Property Management Company looking for a high-end business card, letterhead and envelope design.

We provide high-end / boutique property management for real estate investors or individuals looking for someone to manage their portfolio. we are looking for a cohesive high-end design for our business cards, letterhead and envelopes.

Target Market(s)

Real Estate Investors

Industry/Entity Type

Real Estate

Requirements
Must have
• business card, letterhead and envelope design - logo attached

```html
<!DOCTYPE html>
<html lang="en">
<head>
<meta charset="utf-8">
<title>Northvale Property Management – Business Card</title>
<link rel="stylesheet" href="https://fonts.googleapis.com/css2?family=Roboto:wght@400;500;700&display=swap">
<style>
  :root {
    --page-bg: #e6e6e6;
    --card-white: #ffffff;
    --card-dark: #2b2b2b;
    --name-blue: #0f4a84;
    --icon-blue: #1c5c9c;
    --title-grey: #9a9a9a;
    --address-grey: #555555;
    --contact-white: #ffffff;
    --brand-silver: #d9d9d9;
  }
  * { margin: 0; padding: 0; box-sizing: border-box; }
  html, body {
    width: 1125px; height: 1200px; overflow: hidden;
    background: var(--page-bg);
    font-family: "Roboto", Arial, sans-serif;
  }
  .canvas { position: relative; width: 1125px; height: 1200px; }

  .card {
    position: absolute; left: 150px; width: 826px; height: 472px;
    overflow: hidden;
  }
  .card-front { top: 98px; background: var(--card-white); }
  .card-back { top: 631px; background: var(--card-dark); }

  .front-band {
    position: absolute; left: 0; right: 0; bottom: 0; height: 190px;
    background: var(--card-dark);
  }

  .identity {
    position: absolute; right: 508px; top: 92px; text-align: right;
  }
  .identity .person-name {
    color: var(--name-blue); font-weight: 700; font-size: 27px; line-height: 1.1;
  }
  .identity .person-title {
    color: var(--title-grey); font-weight: 500; font-size: 18px; margin-top: 4px;
  }

  .address {
    position: absolute; right: 540px; top: 170px; text-align: right;
    color: var(--address-grey); font-size: 18px; line-height: 23px;
  }
  .address-icon { position: absolute; left: 300px; top: 176px; width: 16px; height: 22px; }

  .contact-list {
    position: absolute; left: 0; top: 318px; width: 330px; list-style: none;
  }
  .contact-list li {
    position: relative; height: 23.5px; padding-right: 54px; text-align: right;
    color: var(--contact-white); font-size: 18px; line-height: 23.5px;
  }
  .contact-list svg {
    position: absolute; right: 10px; top: 5px; width: 15px; height: 15px;
    fill: var(--icon-blue);
  }

  .brand {
    position: absolute; left: 0; right: 0; top: 208px; text-align: center;
    color: var(--brand-silver); font-weight: 500;
  }
  .brand .brand-name { font-size: 50px; letter-spacing: 11px; line-height: 1; }
  .brand .brand-tagline { font-size: 26px; letter-spacing: 6px; margin-top: 8px; }
</style>
</head>
<body>
<div class="canvas">

  <section class="card card-front">
    <div class="front-band"></div>

    <div class="identity">
      <div class="person-name">Daniel Harper</div>
      <div class="person-title">President</div>
    </div>

    <div class="address">4120 Birchwood Court<br>Fairview, Oregon 97024</div>
    <svg class="address-icon" viewBox="0 0 16 22" aria-hidden="true">
      <path fill="var(--icon-blue)" d="M8 0C3.6 0 0 3.5 0 7.8 0 13.5 8 22 8 22s8-8.5 8-14.2C16 3.5 12.4 0 8 0zm0 11a3.2 3.2 0 1 1 0-6.4A3.2 3.2 0 0 1 8 11z"/>
    </svg>

    <ul class="contact-list">
      <li>555-014-2288
        <svg viewBox="0 0 16 16" aria-hidden="true"><path d="M3.5 1l2.6 2.8-1.4 2.1c.9 1.9 2.5 3.5 4.4 4.4l2.1-1.4L14 11.5 12.3 14C6.4 13.7 2.3 9.6 2 3.7z"/></svg>
      </li>
      <li>555-019-7731
        <svg viewBox="0 0 16 16" aria-hidden="true"><path d="M4 0h8a1 1 0 0 1 1 1v14a1 1 0 0 1-1 1H4a1 1 0 0 1-1-1V1a1 1 0 0 1 1-1zm1 2v10h6V2zm3 11a1 1 0 1 0 0 2 1 1 0 0 0 0-2z"/></svg>
      </li>
      <li>555-016-4402
        <svg viewBox="0 0 16 16" aria-hidden="true"><path d="M4 1h8v4H4zM1 6h14v7h-2v-3H3v3H1zm3 5h8v4H4z"/></svg>
      </li>
      <li>hello@northvale.com
        <svg viewBox="0 0 16 16" aria-hidden="true"><path d="M1 3h14v1.3L8 9 1 4.3zm0 3l7 4.6L15 6v7H1z"/></svg>
      </li>
      <li>www.northvale.com
        <svg viewBox="0 0 16 16" aria-hidden="true"><path d="M8 1a7 7 0 1 0 0 14A7 7 0 0 0 8 1zm0 1.5c.7 0 1.6 1.4 1.9 3.5H6.1C6.4 3.9 7.3 2.5 8 2.5zM2.6 7h3.3v2H2.6a5.5 5.5 0 0 1 0-2zm3.5 3h3.8C9.6 12.1 8.7 13.5 8 13.5s-1.6-1.4-1.9-3.5zM10.1 7h3.3a5.5 5.5 0 0 1 0 2h-3.3z"/></svg>
      </li>
    </ul>
  </section>

  <section class="card card-back">
    <div class="brand">
      <div class="brand-name">NORTHVALE</div>
      <div class="brand-tagline">PROPERTY MANAGEMENT</div>
    </div>
  </section>

</div>
</body>
</html>
```